UK VoIP Services Provider needs A5 Flyer design

We require a really good flyer A5 to sell our new "Wirelo Hub" product

Our company "The Linkhaven Store" provide Low cost International Calls to people all over the world with our mobile calling apps. We also provide business in the UK with Phone Systems.

Our latest product the "Wirelo Hub" provides small businesses and business who operate from home a low cost phone line with a free number.

Please see my website: www.thelinkhavenstore.co.uk. Here you can see the style of my site

I have attached our branding guidelines in a PSD

We have also attached an old flyer we had designed two years ago "LinkhavenStore A5 Flyer" just to give you some insight into our products

This flyer is for my "Wirelo Hub" product:

Here is the landing page

http://www.thelinkhavenstore.co.uk/home-wirelo-services-from-the-linkhaven-store

You can see the benefits of the product on that page above and how it works

Here are the call plans you can have with the Wirelo Hub and you can also have an incoming number from 55 countries

http://www.thelinkhavenstore.co.uk/business-call-packages

http://www.thelinkhavenstore.co.uk/international-calls

What does a VoIP do? How does it help you communicate?

This is a Wirelo Hub that allows small business to have a FREE phone line and FREE incoming number. It routes calls over your existing broadband and the call charges are up to 90% cheaper

I have attached my company logo and some text content on a word document. Please note the content in the word documents are text content. Please avoid too much "copy and paste" We need you to "design"

I have also attached some pictures of the voip boxes as we have two options

Also we have a diagram of "how it works" attached in the content word document flles

Here is a company that provides the same products and services as us: www.telquora.co.uk. Just thought it may be useful for ideas. I have also attached a graphic from this company called "VoIP_Calling___Telquora_UK" for inspiration and ideas

Any questions please feel free to contact me anytime
Updates

Having looked at all the designs, they are all missing the essence of the product which is aimed at businesses that have been set up from home or are in a small office who require a 2nd phone line to separate their business from the home phone line. One of the benefits of this is that it allows them to portray a more professional image to clients. The Leaflet itself needs to look more professional and not so brash. We are still aiming at professional business people such as architects etc who might work from home. Please soften the feel of the leaflet. I will attach a rough "sketch" of what we are trying to achieve. Perhaps the image might give some guidance as well. Although the free part of the message is a strong proposition, a second line with minimal cost that will help the business owner is also a strong proposition. i.e FREE BUSINESS PHONE LINES FOR YOUR HOME/SMALL OFFICE. Be more professional with dedicated Second Phone line for your home/small business Wirelo Hub* from the linkhaven store for business is a simple cost effective solution for small business, designed for today's flexible working environment. With zero line rental and no lengthy contracts it is ideal for small business start ups, home businesses or any business that does not want to miss a single call. With the Wirelo Hub you use the internet to bypass traditional phone networks and dramatically cut the cost of UK and International phone calls.

Reason: We need more time to work with the designers and get more designs as only a few designers have submitted designs Thanks RM

Target Market(s)

Small Businesses.

Small offices

Businesses who operate from home

This solution is ideal as it gives you a phone line for free with no line rental or install costs. The Wirelo Hub simply plugs into a broadband connection and you have a phone line available to receive and make calls. We also provide a FREE UK number

Our call costs are very low as well

Industry/Entity Type

Small Business

Font styles to use
Other font styles liked:
• Plesae see the file "voip font styles" for our branding guidlines

Requirements
Must have
• Two sided A5 flyer

Use of text
Bullet points
Our attached Logo
Pictures/Images
Nice to have
• We are open to ideas

```html
<!DOCTYPE html>
<html lang="en">
<head>
<meta charset="utf-8">
<title>The Linkhaven Store – Free Phone Lines Flyer</title>
<link rel="stylesheet" href="https://fonts.googleapis.com/css2?family=Baloo+2:wght@800&family=Nunito+Sans:wght@400;600&display=swap">
<style>
  :root {
    --stage: #2e2e2e;
    --paper: #ffffff;
    --cyan: #2fb0e0;
    --teal: #1a6f8e;
    --navy: #123f57;
    --ink: #222a30;
    --photo-a: #b9c3c8;
    --photo-b: #e7ecee;
  }
  * { box-sizing: border-box; margin: 0; padding: 0; }
  html, body { width: 907px; height: 1200px; overflow: hidden; background: var(--stage); }
  .flyer {
    position: absolute; left: 73px; top: 62px; width: 762px; height: 1068px;
    background: var(--paper); overflow: hidden;
    font-family: "Nunito Sans", Arial, sans-serif; color: var(--ink);
  }
  .flyer-shapes { position: absolute; inset: 0; }
  .brand {
    position: absolute; left: 36px; top: 44px; display: flex; align-items: center; gap: 14px;
  }
  .brand-dot { width: 74px; height: 74px; border-radius: 50%; border: 9px solid var(--cyan); }
  .brand-name {
    color: var(--cyan); font-weight: 600; font-size: 34px; line-height: 32px; letter-spacing: -0.5px;
  }
  .audience { position: absolute; left: 36px; top: 218px; width: 360px; color: var(--navy); }
  .audience h2 { font-weight: 600; font-size: 27px; line-height: 35px; }
  .audience p { color: #fff; font-size: 17px; line-height: 22px; margin-top: 2px; }
  .headline {
    position: absolute; right: 34px; top: 208px; text-align: right;
    font-family: "Baloo 2", "Arial Rounded MT Bold", sans-serif; font-weight: 800;
    font-size: 86px; line-height: 70px; color: var(--navy); letter-spacing: 1px;
  }
  .photo {
    position: absolute; left: 17px; width: 340px; height: 205px;
    border: 7px solid var(--cyan); border-radius: 16px;
    box-shadow: 0 3px 6px rgba(0,0,0,0.35);
  }
  .photo-office { top: 443px; background: linear-gradient(135deg, var(--photo-b), var(--photo-a) 60%, #8d9aa1); }
  .photo-handsets { top: 698px; background: linear-gradient(180deg, #d9dcd8, #a4a7a2 55%, #6c6b66); }
  .benefits { position: absolute; left: 406px; top: 488px; width: 340px; list-style: none; }
  .benefits li {
    display: flex; gap: 9px; font-size: 19px; line-height: 26px; margin-bottom: 10px;
  }
  .benefits svg { flex: none; width: 24px; height: 26px; margin-top: 1px; }
</style>
</head>
<body>
<main class="flyer">
  <svg class="flyer-shapes" width="762" height="1068" viewBox="0 0 762 1068" aria-hidden="true">
    <!-- header bands -->
    <path d="M0 0 H762 V116 H430 C380 116 372 36 318 36 H0 Z" fill="var(--teal)"/>
    <path d="M0 44 H318 C366 44 376 124 430 124 H762" fill="none" stroke="var(--cyan)" stroke-width="4"/>
    <path d="M440 132 H762 V160 H470 C455 160 452 132 440 132 Z" fill="var(--cyan)"/>
    <rect x="0" y="176" width="762" height="8" fill="var(--cyan)"/>
    <rect x="0" y="188" width="762" height="8" fill="var(--teal)"/>
    <!-- headline panel -->
    <path d="M0 200 H762 V432 H480 C420 432 410 353 350 353 H0 Z" fill="var(--cyan)"/>
    <path d="M0 362 H350 C405 362 415 441 480 441 H762" fill="none" stroke="var(--teal)" stroke-width="3"/>
    <path d="M0 372 H350 C400 372 412 452 480 452 H762" fill="none" stroke="var(--teal)" stroke-width="2"/>
    <!-- footer bands -->
    <path d="M0 922 H360 C400 922 405 955 440 955 H0 Z" fill="var(--cyan)"/>
    <path d="M0 955 H360 C395 955 410 1000 450 1000 H762 V1035 H0 Z" fill="var(--cyan)"/>
    <path d="M0 945 H362 C398 945 408 960 420 975 C432 960 440 952 470 952 H762" fill="none" stroke="var(--teal)" stroke-width="3"/>
    <rect x="0" y="1045" width="762" height="23" fill="var(--cyan)"/>
  </svg>

  <div class="brand">
    <span class="brand-dot"></span>
    <span class="brand-name">the<br>linkhaven<br>store</span>
  </div>

  <section class="audience">
    <h2>Which Businesses can benefit from this:</h2>
    <p>Anyone that has broadband service and never wants to miss a single call again</p>
  </section>

  <h1 class="headline">FREE<br>PHONE<br>LINES</h1>

  <div class="photo photo-office" role="img" aria-label="Photo of a smiling man on the phone at an office desk with a computer"></div>
  <div class="photo photo-handsets" role="img" aria-label="Photo of two cordless business handsets and a base station on a desk"></div>

  <ul class="benefits">
    <li><svg viewBox="0 0 24 26"><path d="M12 1 23 7v12L12 25 1 19V7Z" fill="var(--teal)"/><path d="M7 13l4 4 6-8" stroke="#fff" stroke-width="2.4" fill="none"/></svg>No line rental, lengthy contracts or hidden charges</li>
    <li><svg viewBox="0 0 24 26"><path d="M12 1 23 7v12L12 25 1 19V7Z" fill="var(--teal)"/><rect x="6" y="9" width="12" height="8" rx="1" fill="#fff"/></svg>Save up to 95% on International and local calls</li>
    <li><svg viewBox="0 0 24 26"><path d="M12 1 23 7v12L12 25 1 19V7Z" fill="var(--teal)"/><circle cx="12" cy="13" r="5" fill="#fff"/></svg>Complete cost tracking with self billing portal</li>
    <li><svg viewBox="0 0 24 26"><path d="M12 1 23 7v12L12 25 1 19V7Z" fill="var(--teal)"/><path d="M7 13l4 4 6-8" stroke="#fff" stroke-width="2.4" fill="none"/></svg>Choose your monthly call plan to suit you</li>
    <li><svg viewBox="0 0 24 26"><path d="M12 1 23 7v12L12 25 1 19V7Z" fill="var(--teal)"/><circle cx="12" cy="13" r="5" fill="none" stroke="#fff" stroke-width="2"/></svg>High quality calls</li>
    <li><svg viewBox="0 0 24 26"><path d="M12 1 23 7v12L12 25 1 19V7Z" fill="var(--teal)"/><rect x="7" y="7" width="10" height="12" fill="none" stroke="#fff" stroke-width="2"/></svg>Dedicated local or national business number</li>
    <li><svg viewBox="0 0 24 26"><path d="M12 1 23 7v12L12 25 1 19V7Z" fill="var(--teal)"/><path d="M7 15a5 5 0 0 1 10 0" stroke="#fff" stroke-width="2.4" fill="none"/></svg>Free UK based Customer Support</li>
    <li><svg viewBox="0 0 24 26"><path d="M12 1 23 7v12L12 25 1 19V7Z" fill="var(--teal)"/><path d="M12 6v14M7 11l5-5 5 5" stroke="#fff" stroke-width="2.2" fill="none"/></svg>Flexible working</li>
  </ul>
</main>
</body>
</html>
```